Two (Similar) Posters - Both 11" x 17"

We are looking for two posters - both 11" x 17" (vertical orientation) - to promote two consecutive, cardiology-related events:

Poster #1) The Inaugural New York RMC Quizline Competition, Cocktail Reception and Whiskey Tasting (http://brelvan-hsq.org/quizline-and-reception)

and

Poster #2) The 89th Annual Scientific Session and 27th Annual Meeting (http://brelvan-hsq.org/2017annualmtg)

#1 is a cocktail party with a whiskey tasting that will also feature a gameshow-like event with the med students, and #2 is an educational conference for doctors

Target Market(s)

Healthcare providers (Please do not include stock images of medical professionals; in fact, please use caution with any stock imagery, as it most likely will not be appropriate.)

Industry/Entity Type

Education

Colors

Designer to choose colors to be used in the design.

Requirements
Must have
• Each poster design should include:
• - the 4 logos of the participating organizations (I can upload various other versions if needed) along with the "wording" that goes alongside each one (see "STD_small" image as an example)
• - name of event
• - date, time and location
• - where to register
• - where to get more information
• - some artistic flavor or detailing
• Final (raw) files in an .ai, .psd, .eps or .idml format are required upon project completion.
Nice to have
• It's not crucial that these two posters "match," but it would be nice if they at least coordinated with each other. Would be nice if the designer could stay close to our color scheme (can be found here - http://brelvan-hsq.org/), but this isn't crucial. Posters should be upscale, neat and professional.
Should not have
• Should not be too difficult to read. These are posters that will likely be hanging on a bulletin board in hospital staff break rooms. Should not be too cartoon-like or silly. The two should not look EXACTLY the same in case people think that they are the same poster.

```html
<!DOCTYPE html>
<html lang="en">
<head>
<meta charset="utf-8">
<title>New York RMC Quizline Competition</title>
<link rel="stylesheet" href="https://fonts.googleapis.com/css2?family=Roboto+Condensed:wght@700&family=Open+Sans:wght@600;700&family=Tinos:ital@0;1&display=swap">
<style>
:root{
  --navy:#0f2469;
  --navy-deep:#07174f;
  --navy-bright:#1b5bb8;
  --gold:#ecd873;
  --band:#e9df7c;
  --ink:#111;
  --white:#fff;
  --rule:rgba(255,255,255,.45);
}
*{margin:0;padding:0;box-sizing:border-box}
html,body{width:1200px;height:1200px;overflow:hidden;background:#fff}
.poster{
  position:absolute;left:226px;top:22px;width:748px;height:1155px;overflow:hidden;
  background:linear-gradient(180deg,#e8de7c 0%,#e2d676 22%,#c9c08a 40%,#8c8d86 55%,#4f586f 68%,#2b3a64 80%,#1c2c5c 100%);
  font-family:"Open Sans",sans-serif;
}
.corner{
  position:absolute;top:0;width:205px;height:174px;border-radius:0 0 8px 8px;
  background:radial-gradient(circle at 50% 45%,var(--navy-bright) 0%,var(--navy) 55%,var(--navy-deep) 100%);
  box-shadow:0 5px 0 rgba(0,0,0,.55);
  font-family:"Roboto Condensed",sans-serif;font-weight:700;text-align:center;
  display:flex;flex-direction:column;justify-content:center;line-height:1;
}
.corner--date{left:22px}
.corner--time{left:527px;width:195px}
.corner .accent{color:var(--gold);font-size:21px}
.corner .big{color:var(--white);font-size:32px}
.corner .num{color:var(--white);font-size:42px}
.corner--time .big{font-size:30px}
.disc-shadow{position:absolute;left:107px;top:64px;width:548px;height:548px;border-radius:50%;background:#1a1a1a}
.disc{position:absolute;left:102px;top:58px;width:544px;height:544px;border-radius:50%;
  background:radial-gradient(circle at 50% 40%,#fff 0%,#f3f3f3 60%,#dedede 100%)}
.title{position:absolute;left:0;width:748px;text-align:center;font-family:"Roboto Condensed",sans-serif;font-weight:700;line-height:1;letter-spacing:-.5px}
.title--lead{top:180px;font-size:64px;color:var(--ink)}
.title--name{top:248px;font-size:66px;color:var(--navy)}
.title--event{top:306px;font-size:104px;color:var(--navy)}
.title--kind{top:392px;font-size:76px;color:var(--navy)}
.ribbon{position:absolute;left:0;top:440px;width:748px;height:130px}
.ribbon-text{position:absolute;left:94px;top:498px;width:560px;text-align:center;font-family:"Roboto Condensed",sans-serif;font-weight:700;font-size:33px;color:var(--white)}
.info{position:absolute;left:0;width:748px;text-align:center}
.label{color:var(--white);font-size:18px;font-weight:700}
.label::after{content:"";display:block;width:150px;height:1px;margin:5px auto 0;background:var(--rule)}
.value{color:var(--gold);font-weight:700}
.rule{position:absolute;left:46px;width:656px;height:1px;background:var(--rule)}
.cost{top:637px}
.cost .value{font-size:24px;line-height:34px;margin-top:8px}
.place{top:763px}
.place .value{font-size:24px;margin-top:6px}
.register{top:849px}
.register .value{font-size:31px;margin-top:4px}
.contact{top:958px}
.contact .lead{color:var(--white);font-size:19px;font-weight:600}
.contact .value{font-size:27px;margin-top:2px}
.partners{position:absolute;left:0;bottom:0;width:748px;height:107px;background:var(--band);
  font-family:"Tinos",serif;color:var(--ink)}
.partner{position:absolute;top:28px;display:flex;align-items:center;gap:6px}
.partner .mark{width:44px;height:44px;border-radius:50%;background:var(--navy);flex:none}
.partner .mark--light{background:#c9c08a}
.partner .name{font-family:"Open Sans",sans-serif;font-weight:700;font-size:8.6px;line-height:11px;color:var(--navy)}
.partner .intro{display:block;font-family:"Tinos",serif;font-style:italic;font-weight:400;font-size:9px;color:var(--ink);margin-bottom:6px}
.p1{left:46px}.p2{left:214px}.p3{left:370px}.p4{left:552px}
</style>
</head>
<body>
<main class="poster">
  <div class="disc-shadow"></div>
  <div class="disc"></div>

  <div class="corner corner--date">
    <span class="accent">Wednesday</span>
    <span class="num">6</span>
    <span class="big">December</span>
    <span class="big">2017</span>
  </div>
  <div class="corner corner--time">
    <span class="accent">from</span>
    <span class="big">6:30p.m.</span>
    <span class="accent">to</span>
    <span class="big">10:30p.m.</span>
  </div>

  <h1>
    <span class="title title--lead">The Inaugural</span>
    <span class="title title--name">New York RMC</span>
    <span class="title title--event">Quizline</span>
    <span class="title title--kind">Competition</span>
  </h1>

  <svg class="ribbon" viewBox="0 0 748 130" aria-hidden="true">
    <polygon points="18,12 120,12 120,92 40,92 70,52" fill="#000"/>
    <polygon points="730,12 628,12 628,92 708,92 678,52" fill="#000"/>
    <polygon points="94,12 120,26 120,40 94,40" fill="#333"/>
    <polygon points="654,12 628,26 628,40 654,40" fill="#333"/>
    <rect x="94" y="24" width="560" height="98" fill="#000"/>
  </svg>
  <div class="ribbon-text">Cocktail Reception &amp; Whiskey Tasting</div>

  <section class="info cost">
    <div class="label">Cost</div>
    <div class="value">Free for NYRMC/RMC Members<br>$30 for nonmembers and guests</div>
  </section>
  <div class="rule" style="top:757px"></div>

  <section class="info place">
    <div class="label">Place</div>
    <div class="value">Alder &amp; Vane, 14 E 41st St, New York, NY 10017</div>
  </section>
  <div class="rule" style="top:842px"></div>

  <section class="info register">
    <div class="label">Register online at</div>
    <div class="value">brelvan-hsq.org/2017annualmtg</div>
  </section>
  <div class="rule" style="top:940px"></div>

  <section class="info contact">
    <div class="lead">For more information / to inquire about becoming an exhibitor</div>
    <div class="value">call : (212) 555-0148 / email : ask@brelvan-hsq.org</div>
  </section>

  <footer class="partners">
    <div class="partner p1"><span class="mark"></span><span class="name">RMC Chapter Exchange<br>Program<br>New York, Lisbon</span></div>
    <div class="partner p2"><span class="mark mark--light"></span><span class="name"><span class="intro">Presented by</span>The Brelvan<br>Cardiology Society, Inc.</span></div>
    <div class="partner p3"><span class="mark"></span><span class="name"><span class="intro">of the</span>New York State Chapter,<br>Royal Meridian College</span></div>
    <div class="partner p4"><span class="mark mark--light"></span><span class="name"><span class="intro">In Association with</span>Halden Heart Center</span></div>
  </footer>
</main>
</body>
</html>
```